Arcade grab machine rebrand

We need the attached arcade grab machine rebranded. It is currently named "Marbled Otter" but we would like to rebrand it something like "Juniper Twirl" (as the machine actually changes colour). We would like it to be much more colourful and modern than the original artwork (hence new name) so it stands out a much more. The oval top sign and 2 x side stickers need to be designed, dimensions attached

```html
<!DOCTYPE html>
<html lang="en">
<head>
<meta charset="utf-8">
<title>Juniper Twirl – Cabinet Artwork</title>
<link rel="stylesheet" href="https://fonts.googleapis.com/css2?family=Lilita+One&display=swap">
<style>
  :root {
    --page: #ffffff;
    --brand: #d81f3a;
    --oval-rim: #b13ec4;
    --cabinet-lilac: #e6d2f2;
    --cabinet-glow: #c9e08a;
    --prize-yellow: #f5d53a;
    --swirl-red: #ee3b3b;
    --swirl-orange: #f7942a;
    --swirl-yellow: #f6e04a;
    --swirl-white: #fbfbf4;
    --swirl-green: #4cc49a;
    --swirl-cyan: #4bb8e4;
    --swirl-blue: #2f5fb5;
    --swirl-violet: #7a4bb8;
  }
  html, body {
    margin: 0;
    padding: 0;
    width: 1200px;
    height: 1000px;
    overflow: hidden;
    background: var(--page);
  }
  .sheet {
    position: relative;
    width: 1200px;
    height: 1000px;
    font-family: "Lilita One", "Arial Rounded MT Bold", sans-serif;
  }
  .swirl {
    background:
      radial-gradient(ellipse at 40% 45%, rgba(255,255,255,.95) 0%, rgba(255,255,255,.55) 18%, rgba(255,255,255,0) 42%),
      linear-gradient(100deg, var(--swirl-red) 0%, var(--swirl-orange) 14%, var(--swirl-yellow) 28%, var(--swirl-white) 45%, var(--swirl-green) 62%, var(--swirl-cyan) 76%, var(--swirl-blue) 92%, var(--swirl-violet) 100%);
  }
  .cabinet-photo {
    position: absolute;
    left: 150px;
    top: 65px;
    width: 385px;
    height: 870px;
    border-radius: 90px 90px 10px 10px;
    background:
      linear-gradient(180deg, var(--cabinet-lilac) 0%, var(--cabinet-lilac) 16%, var(--cabinet-glow) 30%, var(--prize-yellow) 55%, var(--cabinet-lilac) 72%, var(--cabinet-lilac) 100%);
  }
  .panel {
    position: absolute;
    overflow: hidden;
    box-shadow: 0 4px 14px rgba(0,0,0,.28);
    display: flex;
    align-items: center;
    justify-content: center;
  }
  .wordmark {
    color: var(--brand);
    font-weight: 400;
    line-height: .95;
    text-align: center;
    white-space: nowrap;
  }
  .top-sign {
    left: 665px;
    top: 100px;
    width: 389px;
    height: 186px;
    border-radius: 50%;
    border: 4px solid var(--oval-rim);
  }
  .top-sign .wordmark { font-size: 48px; }
  .side-strip {
    left: 662px;
    top: 343px;
    width: 396px;
    height: 122px;
    justify-content: flex-start;
    align-items: flex-start;
  }
  .side-strip .wordmark {
    font-size: 24px;
    margin: 18px 0 0 26px;
  }
  .front-strip {
    left: 731px;
    top: 500px;
    width: 247px;
    height: 90px;
    align-items: flex-start;
  }
  .front-strip .wordmark {
    font-size: 11px;
    margin-top: 10px;
    margin-left: 20px;
  }
  .base-panel {
    left: 659px;
    top: 627px;
    width: 401px;
    height: 309px;
  }
  .base-panel .wordmark { font-size: 62px; margin-left: 20px; }
  .brand-lockup {
    position: absolute;
    left: 18px;
    top: 888px;
    display: flex;
    align-items: flex-start;
  }
  .brand-lockup .wordmark { font-size: 38px; }
  .trademark {
    font-family: Arial, sans-serif;
    font-size: 12px;
    color: #555;
    margin-left: 4px;
    margin-top: 4px;
  }
</style>
</head>
<body>
  <main class="sheet">
    <div class="cabinet-photo" role="img" aria-label="Photograph of the lilac grab machine cabinet filled with yellow prizes, wearing the Juniper Twirl top sign and side artwork"></div>

    <section class="panel top-sign swirl" role="img" aria-label="Rainbow swirl background of the oval top sign">
      <div class="wordmark">Juniper<br>Twirl</div>
    </section>

    <section class="panel side-strip swirl" role="img" aria-label="Rainbow swirl background of the upper side sticker">
      <div class="wordmark">Juniper<br>Twirl</div>
    </section>

    <section class="panel front-strip swirl" role="img" aria-label="Rainbow swirl background of the narrow front sticker">
      <div class="wordmark">Juniper<br>Twirl</div>
    </section>

    <section class="panel base-panel swirl" role="img" aria-label="Rainbow swirl background of the lower side panel">
      <div class="wordmark">Juniper<br>Twirl</div>
    </section>

    <div class="brand-lockup">
      <div class="wordmark">Juniper<br>Twirl</div>
      <span class="trademark">™</span>
    </div>
  </main>
</body>
</html>
```